Great Opportunity !! Masters in Business Analytics College Course

the size is Full Page, with bleed*
8”x 10.75" plus 0.25" bleed.
please leave one inch for footer
the purpose is attract students to join this college program .
this is for students in USA .
college age of around 24 years old
I am looking for a flyer that is unique and shows creativity .
A flyer that people would want to look at it because it is unique.
you can choose either vector, text ,or picture.
if you do picture it should be a white USA citizen wearing a white solid shirt and not long hair

Target Market(s)

USA students about 23 in age to join this college program

Industry/Entity Type

education

Colors
0054AA
0677BA
7BADD7
CADEEF
E8F1F8
0094D4
00A9DD
6FCCEA
C7EBF8
E9F6FB

Requirements
Must have
• the text should not be crowded .. .. .. the ad should not be full of text
Should not have
• not have very large text .. it should not be a flyer that is full of text .. you have to figure out how to avoid looking at the ad and it is very busy with text

```html
<!DOCTYPE html>
<html lang="en">
<head>
<meta charset="utf-8">
<title>Master's in Business Analytics – Open House Flyer</title>
<link rel="stylesheet" href="https://fonts.googleapis.com/css2?family=Montserrat:wght@400;500;600;700;800&display=swap">
<style>
  :root {
    --stage: #13234a;
    --paper: #f7f8fa;
    --ink: #262a33;
    --navy: #2a5ea8;
    --sky: #36c8f0;
    --pink: #e0256a;
    --pink-light: #f0579c;
    --pink-deep: #d81d5e;
    --program-blue: #2e4aa0;
    --orange: #f7a21b;
  }
  * { margin: 0; padding: 0; box-sizing: border-box; }
  html, body { width: 1200px; height: 1200px; overflow: hidden; background: var(--stage); }
  body { font-family: "Montserrat", sans-serif; color: var(--ink); position: relative; }

  .flyer {
    position: absolute; left: 186px; top: 52px;
    width: 1334px; height: 1766px;
    transform: scale(0.621); transform-origin: 0 0;
    background: linear-gradient(135deg, #ffffff 0%, var(--paper) 55%, #eef0f3 100%);
    overflow: hidden;
  }
  .block { position: absolute; left: 0; width: 100%; text-align: center; white-space: nowrap; }

  .headline {
    position: absolute; left: 120px; top: 80px; width: 1090px; height: 175px;
    border-radius: 16px;
    background: linear-gradient(90deg, var(--navy) 0%, #2c86cc 55%, var(--sky) 100%);
    color: #fff; font-weight: 700; text-align: center; white-space: nowrap;
    display: flex; flex-direction: column; justify-content: center; line-height: 1.12;
    letter-spacing: -0.5px;
  }
  .headline .line-1 { font-size: 54px; }
  .headline .line-2 { font-size: 66px; }

  .program-name { top: 285px; font-size: 32px; line-height: 44px; }
  .salary-claim { top: 386px; font-size: 33px; font-weight: 600; color: var(--pink); }
  .salary-source { top: 443px; font-size: 21px; }

  .roles {
    position: absolute; left: 205px; top: 493px; width: 918px; height: 58px;
    border-radius: 14px;
    background: linear-gradient(90deg, var(--navy) 0%, var(--sky) 55%, var(--navy) 100%);
    color: #fff; font-size: 25px; white-space: nowrap;
    display: flex; align-items: center; justify-content: center; gap: 18px;
  }

  .hired-title { top: 570px; font-size: 32px; font-weight: 700; color: var(--pink); }
  .employers {
    position: absolute; left: 596px; top: 622px; list-style: none; font-size: 28px; line-height: 43.6px; white-space: nowrap;
  }
  .employers li::before {
    content: ""; display: inline-block; width: 9px; height: 9px; border-radius: 50%;
    background: var(--pink); margin-right: 14px; vertical-align: middle; position: relative; top: -3px;
  }

  .open-house {
    position: absolute; left: 486px; top: 861px; width: 360px; height: 70px; border-radius: 12px;
    background: linear-gradient(90deg, var(--pink-deep), var(--pink-light));
    color: #fff; font-size: 46px; font-weight: 700; text-align: center; line-height: 70px; white-space: nowrap;
  }
  .event-details { top: 945px; font-size: 28px; line-height: 43.5px; }
  .accreditation { top: 1067px; font-size: 26px; }
  .accreditation strong { font-weight: 700; }

  .program-title { top: 1158px; font-size: 32px; font-weight: 700; color: var(--program-blue); }
  .program-facts { top: 1204px; font-size: 28px; line-height: 43.5px; }
  .program-location { top: 1300px; font-size: 22px; }

  .corner-art { position: absolute; left: 0; top: 1110px; width: 860px; height: 656px; }
</style>
</head>
<body>
  <main class="flyer">
    <h1 class="headline">
      <span class="line-1">Do you have an analytical mind and</span>
      <span class="line-2">seeking a profitable career?</span>
    </h1>

    <p class="block program-name">A Master's in Business Analytics-<br>Ridgefield State University **</p>
    <p class="block salary-claim">can prepare you for in-demand jobs with a median salary of $100k+</p>
    <p class="block salary-source">(National Labor Data Survey 2023)</p>

    <div class="roles">
      <span>BI Developer</span><span>|</span><span>Data Analyst</span><span>|</span><span>Data Scientist</span><span>|</span><span>Data Developer</span>
    </div>

    <h2 class="block hired-title">Graduates were hired at:</h2>
    <ul class="employers">
      <li>Norvale Pharma</li>
      <li>Brightline Advisory</li>
      <li>Corvex Systems</li>
      <li>Voltaris Motors</li>
      <li>Harborstone Insurance</li>
    </ul>

    <div class="open-house">Open House</div>
    <p class="block event-details">Wednesday, April 20, 7:30 pm.<br>Email info@ridgefieldstate.edu&nbsp; for the link!</p>

    <p class="block accreditation">*** GBSA Accreditation. A distinction held by only <strong>5%</strong> of business schools globally.</p>

    <h2 class="block program-title">Men &amp; Women Program</h2>
    <p class="block program-facts">21 Months<br>Hybrid with one weekly in-person evening meeting</p>
    <p class="block program-location">Brookhaven Falls, NJ, USA &nbsp;·&nbsp; Update location</p>

    <svg class="corner-art" viewBox="0 0 860 656" role="img" aria-label="Decorative cluster of overlapping blue, pink and orange geometric triangles">
      <defs>
        <linearGradient id="cornerTones" x1="0" y1="0" x2="1" y2="1">
          <stop offset="0" stop-color="#f7a21b"/>
          <stop offset="0.3" stop-color="#ec5597"/>
          <stop offset="0.6" stop-color="#36b6ea"/>
          <stop offset="1" stop-color="#2a5ea8"/>
        </linearGradient>
      </defs>
      <path d="M0 0 L120 100 L250 180 L350 300 L480 420 L600 520 L680 560 L740 500 L860 656 L0 656 Z" fill="url(#cornerTones)"/>
    </svg>
  </main>
</body>
</html>
```